Bakery Business Cards

We are in need of business cards for our bakery business--something non-generic that reflects our business and will stand out. We are a wholesale bakery that primarily services in-store bakeries, casinos, schools, distributors, and fund-raising companies. The family business was founded in 1960. (www.marlowsovenworks.com)

```html
<!DOCTYPE html>
<html lang="en">
<head>
<meta charset="utf-8">
<title>Marlow's Ovenworks – Business Cards</title>
<link rel="stylesheet" href="https://fonts.googleapis.com/css2?family=Cinzel:wght@500;600&family=Crimson+Text:ital@1&family=Karla:wght@400;500&display=swap">
<style>
  :root {
    --stage: #2b2b2d;
    --royal: #0a4fd1;
    --royal-deep: #0640b3;
    --sky: #36b6ff;
    --ink: #1c1c1e;
    --paper: #ffffff;
    --slate: #8c8c8f;
    --muted: #d9d9dc;
  }
  * { margin: 0; padding: 0; box-sizing: border-box; }
  html, body {
    width: 1200px; height: 874px; overflow: hidden;
    background: var(--stage);
  }
  .stage {
    position: relative; width: 1200px; height: 874px;
  }
  .card {
    position: absolute; left: 280px; width: 640px; height: 366px;
    border-radius: 22px; overflow: hidden;
  }
  .card svg.bands { position: absolute; inset: 0; }

  /* Front */
  .card-front { top: 54px; background: var(--royal); }
  .front-brand {
    position: absolute; left: 0; right: 0; top: 92px; text-align: center;
    font-family: "Cinzel", serif; font-weight: 600; color: var(--sky);
  }
  .front-brand .brand-name { font-size: 46px; letter-spacing: 2px; line-height: 1.1; }
  .front-brand .brand-since { font-size: 20px; letter-spacing: 3px; margin-top: 8px; }
  .front-tagline {
    position: absolute; left: 0; width: 500px; top: 288px; text-align: center;
    font-family: "Crimson Text", serif; font-style: italic; font-size: 24px;
    color: var(--royal);
  }

  /* Back */
  .card-back { top: 454px; background: var(--ink); }
  .person { position: absolute; left: 40px; top: 42px; }
  .person-name {
    font-family: "Cinzel", serif; font-weight: 500; font-size: 26px;
    color: var(--paper); letter-spacing: 1px;
  }
  .person-role {
    font-family: "Karla", sans-serif; font-size: 14px; color: var(--royal);
    margin-top: -2px;
  }
  .rule-main {
    position: absolute; left: 36px; top: 112px; width: 360px; height: 1px;
    background: var(--muted);
  }
  .contact-list {
    position: absolute; left: 40px; top: 124px; list-style: none;
    font-family: "Karla", sans-serif; font-size: 15px; color: var(--paper);
  }
  .contact-list li { display: flex; align-items: center; gap: 10px; height: 22px; }
  .contact-list svg { width: 13px; height: 13px; fill: var(--royal); }
  .back-brand {
    position: absolute; right: 40px; top: 70px; text-align: center;
    font-family: "Cinzel", serif; font-weight: 600; color: var(--royal);
  }
  .back-brand .brand-name { font-size: 32px; letter-spacing: 1px; line-height: 1.1; }
  .back-brand .brand-since { font-size: 15px; letter-spacing: 2px; margin-top: 6px; }
  .rule-address {
    position: absolute; right: 40px; top: 212px; width: 210px; height: 1px;
    background: var(--muted);
  }
  .address {
    position: absolute; right: 40px; top: 222px; text-align: right;
    font-family: "Karla", sans-serif; font-size: 15px; line-height: 1.35;
    color: var(--paper);
  }
  .specialties {
    position: absolute; left: 0; width: 440px; top: 318px; text-align: center;
    font-family: "Crimson Text", serif; font-style: italic; font-size: 24px;
    color: var(--paper); word-spacing: 4px;
  }
</style>
</head>
<body>
<main class="stage">

  <section class="card card-front" aria-label="Card front">
    <svg class="bands" viewBox="0 0 640 366" aria-hidden="true">
      <polygon points="0,262 528,262 490,366 0,366" fill="var(--paper)"/>
      <polygon points="548,292 640,292 640,366 516,366" fill="var(--slate)"/>
    </svg>
    <div class="front-brand">
      <div class="brand-name">Marlow's Ovenworks</div>
      <div class="brand-since">SINCE 1960</div>
    </div>
    <p class="front-tagline">Serving Sweetness Since 1960</p>
  </section>

  <section class="card card-back" aria-label="Card back">
    <svg class="bands" viewBox="0 0 640 366" aria-hidden="true">
      <polygon points="0,300 470,300 432,366 0,366" fill="var(--royal)"/>
      <polygon points="500,318 640,318 640,366 474,366" fill="var(--slate)"/>
    </svg>

    <div class="person">
      <h1 class="person-name">ELLIS MARLOW</h1>
      <p class="person-role">Founder</p>
    </div>
    <div class="rule-main"></div>

    <ul class="contact-list">
      <li>
        <svg viewBox="0 0 24 24"><path d="M6.6 10.8a15.1 15.1 0 0 0 6.6 6.6l2.2-2.2a1 1 0 0 1 1-.25 11.4 11.4 0 0 0 3.6.57 1 1 0 0 1 1 1V20a1 1 0 0 1-1 1A17 17 0 0 1 3 4a1 1 0 0 1 1-1h3.5a1 1 0 0 1 1 1c0 1.25.2 2.45.57 3.57a1 1 0 0 1-.25 1z"/></svg>
        (555) 014-2736
      </li>
      <li>
        <svg viewBox="0 0 24 24"><path d="M2 5h20v14H2z M2 5l10 8 10-8" stroke="var(--ink)" stroke-width="1.5"/></svg>
        sales@marlowsovenworks.com
      </li>
      <li>
        <svg viewBox="0 0 24 24"><circle cx="12" cy="12" r="10"/><path d="M2 12h20M12 2c3 3 3 17 0 20M12 2c-3 3-3 17 0 20" stroke="var(--ink)" stroke-width="1.5" fill="none"/></svg>
        www.marlowsovenworks.com
      </li>
    </ul>

    <div class="back-brand">
      <div class="brand-name">Marlow's<br>Ovenworks</div>
      <div class="brand-since">SINCE 1960</div>
    </div>

    <div class="rule-address"></div>
    <address class="address">
      Marlow's Ovenworks Since 1960<br>
      1870 Larkspur Ave<br>
      Fairhaven, OK 73100
    </address>

    <p class="specialties">Cobblers | Pies | Cookies</p>
  </section>

</main>
</body>
</html>
```